Coffee Shop needs a fresh new menu

Hi,
I would like a new menu to be designed for our coffee shop.
We display our menu on a television screen, so would need it in a file that would allow us to continue to do so -- I have attached a photo so that you can see our current design, and how it is displayed.

I'd like something that is easy to read, if the design could have a "hipster" feel to it -- we are located at a hospital and University.

I have attached a Word file with what we would like on the menu.

Feel free to contact me if you have any questions.

Thanks,
Liv

Just A4 size will be fine, and no need to include menu 1 and menu 2 - I just put them in as an example of what we already have -- they are our printed menu's. Thanks

Hospital

```html
<!DOCTYPE html>
<html lang="en">
<head>
<meta charset="utf-8">
<title>Ward Brew Cafe Menu</title>
<link href="https://fonts.googleapis.com/css2?family=Lilita+One&family=Special+Elite&display=swap" rel="stylesheet">
<style>
  :root {
    --canvas: #ecebe8;
    --paper: #f3ecdc;
    --paper-edge: #e6dcc4;
    --paper-warm: #efd9ae;
    --paper-warm-edge: #e3c48f;
    --ink: #2c2620;
    --ink-red: #b3262d;
    --brand-red: #c8202b;
    --stroke-orange: #ef8a2c;
    --stroke-orange-light: #f6b25a;
    --band-yellow: #f5cd52;
    --band-yellow-dark: #e8b838;
    --muted: #5b5248;
  }
  * { box-sizing: border-box; margin: 0; padding: 0; }
  html, body { width: 1200px; height: 900px; overflow: hidden; }
  body {
    background: var(--canvas);
    font-family: "Special Elite", "Courier New", monospace;
    color: var(--ink);
    position: relative;
  }
  .menu-page {
    position: absolute;
    top: 68px;
    width: 540px;
    height: 764px;
    overflow: hidden;
    box-shadow: 0 6px 18px rgba(0,0,0,.18);
  }
  .menu-page--drinks {
    left: 45px;
    background: radial-gradient(ellipse at 55% 45%, #fbf7ee 0%, var(--paper) 55%, var(--paper-edge) 100%);
  }
  .menu-page--food {
    left: 615px;
    background: radial-gradient(ellipse at 40% 50%, #f5e4c0 0%, var(--paper-warm) 60%, var(--paper-warm-edge) 100%);
  }

  .brand {
    position: absolute;
    display: flex;
    align-items: center;
    gap: 10px;
    font-family: "Lilita One", "Arial Black", sans-serif;
    color: var(--brand-red);
    font-size: 38px;
    letter-spacing: 1px;
    line-height: 1;
  }
  .brand-dot { width: 22px; height: 22px; border-radius: 50%; background: var(--brand-red); }
  .brand-sub { position: absolute; font-size: 10px; color: var(--muted); letter-spacing: 1px; }

  .contact {
    position: absolute; top: 36px; right: 26px;
    text-align: right; font-size: 13px; line-height: 1.3;
  }
  .contact-line { display: flex; align-items: center; gap: 6px; justify-content: flex-end; font-weight: bold; }
  .contact-note { font-size: 9px; color: var(--muted); }
  .tagline { position: absolute; top: 104px; left: 0; width: 100%; text-align: center; font-size: 10px; color: var(--muted); }

  .photo { position: absolute; }
  .photo--coffee-cup {
    top: 150px; left: 0; width: 190px; height: 250px;
    background: linear-gradient(150deg, #3b1d0f 0%, #6a2f16 30%, #c8202b 55%, #f3ecdc 100%);
    clip-path: polygon(0 8%, 100% 0, 100% 35%, 0 100%);
  }
  .photo--yoghurt-bowl {
    top: 600px; left: 300px; width: 210px; height: 150px;
    border-radius: 50%;
    background: radial-gradient(circle at 55% 40%, #ffffff 0 22%, #d92b36 32%, #b61e2b 48%, #f1b62e 62%, #e8a21c 100%);
  }

  .section-heading {
    position: absolute;
    font-family: "Lilita One", "Arial Black", sans-serif;
    line-height: 1;
  }
  .section-heading--coffee {
    top: 150px; left: 195px; width: 250px; height: 50px;
    background: linear-gradient(90deg, rgba(239,138,44,0) 0%, var(--stroke-orange) 12%, var(--stroke-orange-light) 88%, rgba(246,178,90,0) 100%);
    color: #fff; font-size: 34px; text-align: center; padding-top: 7px; letter-spacing: 1px;
  }
  .section-heading--light,
  .section-heading--breakfast,
  .section-heading--sandwiches {
    background: var(--band-yellow);
    border-bottom: 3px solid var(--band-yellow-dark);
    font-size: 17px; padding: 5px 12px 4px; color: var(--ink);
  }
  .section-heading--light { top: 532px; left: 36px; border-radius: 3px; }
  .section-heading--breakfast { top: 112px; left: 30px; width: 300px; text-align: right; }
  .section-heading--sandwiches { top: 380px; left: 0; width: 320px; text-align: right; padding-right: 24px; }

  .price-list { position: absolute; list-style: none; font-size: 13px; line-height: 21px; }
  .price-list li { display: flex; }
  .price-list--coffee { top: 212px; left: 200px; width: 320px; }
  .price-list--coffee .item { width: 115px; }
  .price-list--coffee .small { width: 110px; text-align: right; }
  .price-list--coffee .large { flex: 1; text-align: right; }
  .price-list--coffee .gap { height: 14px; }
  .price-list--short { top: 404px; left: 300px; width: 220px; }
  .price-list--short li, .price-list--breakfast li, .price-list--sandwiches li { justify-content: flex-end; gap: 8px; }
  .extras { position: absolute; top: 496px; left: 20px; width: 500px; font-size: 10px; text-align: right; white-space: nowrap; }
  .price-list--light { top: 572px; left: 36px; width: 200px; }
  .price-list--light li { justify-content: space-between; }
  .price-list--breakfast { top: 150px; left: 20px; width: 300px; text-align: right; color: var(--ink-red); }
  .price-list--sandwiches { top: 416px; left: 10px; width: 300px; color: var(--ink-red); }

  .notes { position: absolute; top: 692px; left: 20px; width: 290px; font-size: 9px; line-height: 16px; text-align: right; color: var(--ink); white-space: nowrap; }
  .social { position: absolute; display: flex; align-items: center; gap: 6px; font-size: 10px; color: var(--muted); }

  .photo--breakfast-fruit {
    top: 90px; left: 345px; width: 195px; height: 95px;
    background: linear-gradient(120deg, #d8412f 0%, #f2c04c 45%, #f7e2a6 100%);
    border-radius: 6px;
  }
  .photo--eggs-toast {
    top: 195px; left: 350px; width: 180px; height: 110px;
    background: radial-gradient(ellipse at 40% 55%, #fbf2df 0 30%, #f0a63b 48%, #d99a4c 70%, var(--paper-warm) 100%);
    border-radius: 50%;
  }
  .photo--breakfast-plate {
    top: 330px; left: 325px; width: 205px; height: 150px;
    background: radial-gradient(ellipse at 50% 55%, #f6b72b 0 18%, #fff7e6 30%, #d5843a 55%, #c45d1e 72%, #f4f0ea 82%);
    border-radius: 50%;
  }
  .photo--sandwich {
    top: 600px; left: 325px; width: 205px; height: 130px;
    background: radial-gradient(ellipse at 55% 45%, #e7c48a 0 25%, #8a5a2c 45%, #d2a467 70%, #f3d9a6 100%);
    border-radius: 50%;
  }
  .divider { position: absolute; top: 680px; left: 20px; width: 290px; border-top: 2px dashed rgba(44,38,32,.35); }
</style>
</head>
<body>

<section class="menu-page menu-page--drinks">
  <div class="brand" style="top:34px; left:170px;"><span class="brand-dot"></span>Ward Brew</div>
  <div class="brand-sub" style="top:78px; left:205px;">HOSPITAL · UNIVERSITY · CAFE</div>

  <div class="contact">
    <div class="contact-line">
      <svg width="14" height="14" viewBox="0 0 24 24" aria-hidden="true"><path fill="#2c2620" d="M6.6 10.8a15 15 0 0 0 6.6 6.6l2.2-2.2a1 1 0 0 1 1-.25 11.4 11.4 0 0 0 3.6.57 1 1 0 0 1 1 1V20a1 1 0 0 1-1 1A17 17 0 0 1 3 4a1 1 0 0 1 1-1h3.5a1 1 0 0 1 1 1c0 1.25.2 2.45.57 3.6a1 1 0 0 1-.25 1z"/></svg>
      0400 555 018
    </div>
    <div class="contact-note">Call to order</div>
  </div>

  <p class="tagline">We are open seven days across the hospital and university campus</p>

  <div class="photo photo--coffee-cup" role="img" aria-label="Photo of a red takeaway coffee cup with coffee splashing out"></div>

  <h2 class="section-heading section-heading--coffee">Coffee</h2>

  <ul class="price-list price-list--coffee">
    <li><span class="item">Latte</span><span class="small"></span><span class="large"></span></li>
    <li><span class="item">Cappuccino</span><span class="small">small $4.0</span><span class="large">Large $4.50</span></li>
    <li><span class="item">Flat White</span><span class="small">small $4.0</span><span class="large">Large $4.50</span></li>
    <li><span class="item">Long Mach</span><span class="small">small $4.0</span><span class="large">Large $4.50</span></li>
    <li><span class="item">Hot Chocolate</span><span class="small">small $4.0</span><span class="large">Large $4.50</span></li>
    <li class="gap"></li>
    <li><span class="item">Chai Latte</span><span class="small">small $4.50</span><span class="large">Large $5.0</span></li>
    <li><span class="item">Mocha</span><span class="small">small $4.50</span><span class="large">Large $5.0</span></li>
    <li><span class="item">Dirty Chai</span><span class="small">small $5</span><span class="large">Large $5.50</span></li>
  </ul>

  <ul class="price-list price-list--short">
    <li>Espresso <span>$3.50</span></li>
    <li>Short Macchiato <span>$4.0</span></li>
    <li>Piccolo <span>$4.0</span></li>
    <li>Long Macchiato <span>$4.50</span></li>
  </ul>

  <p class="extras">Extras: Soy Milk, Lactose Free Milk, Syrups, Extra Shot, Decaf &nbsp;$0.50 extra</p>

  <h2 class="section-heading section-heading--light">SOMETHING LIGHT:</h2>
  <ul class="price-list price-list--light">
    <li>Mixed Yoghurt <span>$5.50</span></li>
    <li>Chia Pudding <span>$5.50</span></li>
    <li>Fruit Salad <span>$5.50</span></li>
    <li>Banana Bread <span>$4.0</span></li>
    <li>Protein Balls <span>$4.0</span></li>
    <li>Sesame Snack <span>$4.0</span></li>
    <li>Muffins <span>$4.50</span></li>
    <li>Slices <span>$4.0</span></li>
  </ul>

  <div class="photo photo--yoghurt-bowl" role="img" aria-label="Photo of a bowl of yoghurt with strawberries and mint"></div>

  <div class="social" style="top:744px; left:20px;">
    <svg width="14" height="14" viewBox="0 0 14 14" aria-hidden="true"><rect x="1" y="1" width="12" height="12" rx="3" fill="none" stroke="#5b5248" stroke-width="1.5"/></svg>
    @wardbrewcafe
  </div>
</section>

<section class="menu-page menu-page--food">
  <div class="brand" style="top:40px; left:250px; font-size:32px;"><span class="brand-dot"></span>Ward Brew</div>

  <h2 class="section-heading section-heading--breakfast">BREAKFAST ITEMS:</h2>
  <ul class="price-list price-list--breakfast">
    <li>Bacon, Egg and Cheese Roll $6.0</li>
    <li>Ham and Cheese Toastie $5.0</li>
    <li>Cheese and Tomato Toastie $5.0</li>
    <li>Ham and Cheese Croissant $5.50</li>
    <li>Cheese and Tomato Croissant $5.50</li>
    <li>Plain Croissant $3.50</li>
    <li>Hash Brown $2.00</li>
    <li>2 Piece Toast $3.0</li>
    <li>2 Piece Raisin Toast $3.0</li>
  </ul>

  <div class="photo photo--breakfast-fruit" role="img" aria-label="Photo of fresh fruit, orange juice and fries"></div>
  <div class="photo photo--eggs-toast" role="img" aria-label="Photo of boiled eggs in cups with toast"></div>

  <h2 class="section-heading section-heading--sandwiches">FOOD AND SANDWICHES:</h2>
  <ul class="price-list price-list--sandwiches">
    <li>Sandwiches $6.50 - $7.50</li>
    <li>Made Focaccias $8.50</li>
    <li>Wraps $7.50</li>
    <li>Vegetarian Salad $7.50</li>
    <li>Seafood Salad $9.50</li>
    <li>Hot Chips $5.50</li>
    <li>Dim Sim $1.50</li>
    <li>Potato Cake $1.50</li>
    <li>Plain Hamburger $7.50</li>
    <li>Hamburger with the lot $9.0</li>
    <li>Chicken Schnitzel Burger $8.50</li>
  </ul>

  <div class="photo photo--breakfast-plate" role="img" aria-label="Photo of a plate with fried eggs, toast and hash browns"></div>

  <div class="social" style="top:560px; left:360px;">
    <svg width="14" height="14" viewBox="0 0 14 14" aria-hidden="true"><rect x="1" y="1" width="12" height="12" rx="3" fill="none" stroke="#5b5248" stroke-width="1.5"/></svg>
    @wardbrewcafe
  </div>

  <div class="divider"></div>
  <p class="notes">Our store honours the hospital staff discount card<br>10% off for all registered staff<br>Ready to go meals, slices and lots more!</p>

  <div class="photo photo--sandwich" role="img" aria-label="Photo of a chicken sandwich with fries on a wooden board"></div>
</section>

</body>
</html>
```